New LLC consulting company needs a business card design

I need a business card design for new company in Alexandria Virginia called TK Verdant Consulting LLC. The company is focused on consulting for defense and national security issues with expertise in nuclear and space topics. I would like to see designs that are simple and I am open to colors except for brown.

Target Market(s)

All businesses that are seeking consulting help

Industry/Entity Type

Consulting

Contact Information for Business Card

Name of company - TK Verdant Consulting LLC; name (Delia Hawke) President; email: hawkedr41@mailbox-example.net; Phone: 555-271-9043

Requirements
Must have
• The details described above
Nice to have
• I'm open to all ideas
Should not have
• No brown

```html
<!DOCTYPE html>
<html lang="en">
<head>
<meta charset="utf-8">
<title>TK Verdant Consulting LLC – Business Card</title>
<link href="https://fonts.googleapis.com/css2?family=Bebas+Neue&family=Poppins:wght@400;600&display=swap" rel="stylesheet">
<style>
  :root {
    --page-bg: #d4d7dd;
    --brand-blue: #4169e1;
    --accent-salmon: #f2a3a0;
    --card-light: #f1efef;
    --card-light-edge: #e3dfdf;
    --ink-dark: #333333;
    --ink-light: #ffffff;
  }
  html, body {
    margin: 0;
    padding: 0;
    width: 1200px;
    height: 900px;
    overflow: hidden;
    background: var(--page-bg);
  }
  .business-card {
    position: absolute;
    left: 100px;
    top: 141px;
    width: 1000px;
    height: 618px;
    background: linear-gradient(135deg, var(--card-light) 0%, var(--card-light-edge) 100%);
    box-shadow: 0 10px 30px rgba(0,0,0,0.15);
    overflow: hidden;
  }
  .contact-panel {
    position: absolute;
    left: 0;
    top: 0;
    width: 489px;
    height: 618px;
    background: var(--brand-blue);
    color: var(--ink-light);
  }
  .pointer-accent {
    position: absolute;
    left: 388px;
    top: 249px;
    width: 101px;
    height: 117px;
  }
  .person-name {
    position: absolute;
    left: 58px;
    top: 134px;
    margin: 0;
    font-family: "Bebas Neue", sans-serif;
    font-size: 64px;
    line-height: 1;
    font-weight: 400;
    letter-spacing: 0;
  }
  .person-title {
    position: absolute;
    left: 58px;
    top: 194px;
    margin: 0;
    font-family: "Poppins", sans-serif;
    font-size: 28px;
    line-height: 1;
    font-weight: 400;
  }
  .contact-list {
    position: absolute;
    left: 58px;
    top: 402px;
    margin: 0;
    padding: 0;
    list-style: none;
    font-family: "Poppins", sans-serif;
    font-size: 22px;
    line-height: 1;
  }
  .contact-item {
    display: flex;
    align-items: center;
    height: 30px;
    margin-bottom: 12px;
  }
  .contact-icon {
    width: 26px;
    height: 26px;
    margin-right: 14px;
    flex: none;
  }
  .company-mark {
    position: absolute;
    left: 559px;
    top: 230px;
    width: 380px;
  }
  .company-name {
    margin: 0;
    font-family: "Bebas Neue", sans-serif;
    font-size: 112px;
    line-height: 0.9;
    font-weight: 400;
    color: var(--brand-blue);
  }
  .company-type {
    margin: 6px 0 0;
    font-family: "Poppins", sans-serif;
    font-size: 39px;
    line-height: 1;
    font-weight: 600;
    color: var(--ink-dark);
  }
</style>
</head>
<body>
  <div class="business-card">
    <section class="contact-panel">
      <h1 class="person-name">Delia Hawke</h1>
      <p class="person-title">President</p>
      <ul class="contact-list">
        <li class="contact-item">
          <svg class="contact-icon" viewBox="0 0 24 24" aria-hidden="true">
            <path fill="var(--ink-light)" d="M6.6 10.8c1.4 2.8 3.8 5.1 6.6 6.6l2.2-2.2c.3-.3.7-.4 1-.2 1.1.4 2.3.6 3.6.6.6 0 1 .4 1 1V20c0 .6-.4 1-1 1C10.6 21 3 13.4 3 4c0-.6.4-1 1-1h3.5c.6 0 1 .4 1 1 0 1.3.2 2.5.6 3.6.1.3 0 .7-.2 1L6.6 10.8z"/>
            <path fill="none" stroke="var(--ink-light)" stroke-width="1.6" stroke-linecap="round" d="M14 3.5a7 7 0 0 1 6.5 6.5M14 7a3.5 3.5 0 0 1 3 3"/>
          </svg>
          <span>555-271-9043</span>
        </li>
        <li class="contact-item">
          <svg class="contact-icon" viewBox="0 0 24 24" aria-hidden="true">
            <rect x="2" y="5" width="20" height="14" fill="var(--ink-light)"/>
            <path fill="none" stroke="var(--brand-blue)" stroke-width="1.5" d="M2 5l10 8 10-8M2 19l7.5-7M22 19l-7.5-7"/>
          </svg>
          <span>hawkedr41@mailbox-example.net</span>
        </li>
      </ul>
    </section>
    <svg class="pointer-accent" viewBox="0 0 101 117" aria-hidden="true">
      <polygon points="101,0 0,58 101,117" fill="var(--accent-salmon)"/>
    </svg>
    <div class="company-mark">
      <p class="company-name">TK Verdant</p>
      <p class="company-type">CONSULTING LLC</p>
    </div>
  </div>
</body>
</html>
```